Home page in PSD needed for a Business Consultant website

We have been given the mandate to re-do the website: http://www.lumivanconseil.ca/

Deliverable: home page in PSD format in French language

Context: Luc Dorval is a business strategist specializing in marketing, creativity, business development. He helps small and medium companies develop their business through creative marketing strategies.

Some websites we like for your inspiration:

http://www.tallpinegrove.com.au/
http://www.trwadvisory.com.au/
http://fjalladvisors.com.au/
http://www.olubrenix.com/fr

Target Market(s)

B2B: Companies looking on the web for a business consultant who can help them with marketing, business developement, printing needs.

Industry/Entity Type

Business

Requirements
Must have
• Call to action: "Simplifiez votre développement des affaires" (which means "Simplify your business development")
• List of services (main menu)
• Marketing
• Développement des affaires
• Créativité
• Scolaire
• Impression
• Top menu as follow:
• Accueil
• À propos
• Contact

```html
<!DOCTYPE html>
<html lang="fr">
<head>
<meta charset="utf-8">
<title>Lumivan Conseil — Accueil</title>
<link rel="stylesheet" href="https://fonts.googleapis.com/css2?family=Crimson+Text:wght@400;600&display=swap">
<style>
:root{
  --blue:#0a76c2;
  --ink:#222;
  --grey:#8a8a8a;
  --line:#4a4a4a;
  --bg:#fff;
}
*{margin:0;padding:0;box-sizing:border-box}
html,body{width:1182px;height:1200px;overflow:hidden;background:var(--bg)}
body{position:relative;font-family:"Crimson Text",Georgia,serif;color:var(--ink)}

.site-header{position:absolute;left:0;top:0;width:1182px;height:84px;border-bottom:1px solid var(--line)}
.brand{position:absolute;left:155px;top:18px;display:flex;align-items:center;gap:8px}
.brand-mark{width:16px;height:16px;border-radius:50%;background:var(--blue)}
.brand-name{font-size:26px;color:var(--ink);letter-spacing:.5px}
.brand-tag{position:absolute;left:179px;top:52px;font-size:9px;letter-spacing:1.4px;color:#555}

.top-nav{position:absolute;right:30px;top:12px;display:flex;gap:6px;font-size:13px;color:var(--grey)}
.top-nav a{color:var(--grey);text-decoration:none}
.top-nav .sep{color:#bbb}

.main-nav{position:absolute;top:48px;left:444px;display:flex;gap:26px}
.main-nav a{position:relative;font-size:18px;color:var(--ink);text-decoration:none;letter-spacing:.3px;white-space:nowrap}
.main-nav a.is-active{color:var(--blue)}
.main-nav a.is-active::before{content:"";position:absolute;left:0;right:0;top:-48px;height:6px;background:var(--blue)}

.hero{position:absolute;left:0;top:84px;width:1182px;height:418px;border-bottom:1px solid var(--line)}
.hero-photo{position:absolute;left:277px;top:0;width:629px;height:417px;border-left:1px solid #999;border-right:1px solid #999;
  background:linear-gradient(120deg,#e9eef2 0%,#d9c3b0 30%,#f2efea 50%,#c9a48b 70%,#eef1f4 100%)}
.hero-cta{position:absolute;left:0;top:368px;background:rgba(255,255,255,.88);padding:6px 18px 7px 20px;font-size:21px;color:var(--blue);white-space:nowrap}
.hero-arrow{position:absolute;top:189px;width:40px;height:40px;background:var(--blue)}
.hero-arrow.prev{left:0}.hero-arrow.next{right:0}
.hero-arrow svg{display:block}
.hero-dots{position:absolute;left:518px;top:385px;display:flex;gap:6px}
.hero-dots span{width:14px;height:14px;background:#fff}
.hero-dots span.is-current{background:var(--blue)}

.pointer{position:absolute;top:502px;width:0;height:0;border-left:22px solid transparent;border-right:22px solid transparent;border-top:22px solid var(--blue)}

.features{position:absolute;left:276px;top:543px;display:flex}
.feature{width:210px;height:390px;border-left:1px solid var(--blue);padding:0 20px;position:relative}
.feature:last-child{border-right:1px solid var(--blue);width:211px}
.feature h2{font-weight:400;font-size:25px;color:var(--blue);text-align:center;height:38px;line-height:26px;border-bottom:1px solid var(--line);margin-top:-3px;white-space:nowrap}
.feature p{margin-top:23px;font-size:16px;line-height:15.4px;color:var(--blue);text-align:justify;text-indent:33px;hyphens:auto;-webkit-hyphens:auto}
.btn{position:absolute;left:17px;top:360px;width:175px;height:31px;background:var(--blue);color:#fff;font-size:17px;text-align:center;line-height:31px;text-decoration:none;box-shadow:0 5px 4px -3px rgba(0,0,0,.45)}

.band{position:absolute;left:0;top:978px;width:1182px;height:40px;background:var(--blue)}
.site-footer{position:absolute;left:0;top:1018px;width:1182px}
.foot-col{position:absolute;top:14px;width:175px}
.foot-col h3{font-size:17px;font-weight:600;color:var(--grey);margin-bottom:4px}
.foot-col p{font-size:13.5px;line-height:15.4px;color:var(--grey);text-align:justify;text-indent:33px;hyphens:auto;-webkit-hyphens:auto}
.socials{display:flex;gap:8px;margin:6px 0 0 26px}
.socials span{width:24px;height:24px;border-radius:50%;background:#9a9a9a}
.copyright{position:absolute;left:0;top:1165px;width:1182px;border-top:1px solid #888;text-align:center;font-size:13px;color:var(--grey);padding-top:8px}
.copyright strong{font-weight:600}
</style>
</head>
<body>
<header class="site-header">
  <div class="brand"><span class="brand-mark"></span><span class="brand-name">Lumivan Conseil</span></div>
  <div class="brand-tag">commercialisation | marketing | créativité</div>
  <nav class="top-nav" aria-label="Menu principal">
    <a href="#">Accueil</a><span class="sep">|</span><a href="#">À propos</a><span class="sep">|</span><a href="#">Contact</a>
  </nav>
  <nav class="main-nav" aria-label="Services">
    <a href="#" class="is-active">marketing</a>
    <a href="#" class="is-active">développement des affaires</a>
    <a href="#">créativité</a>
    <a href="#">scolaire</a>
    <a href="#">impression</a>
  </nav>
</header>

<section class="hero">
  <div class="hero-photo" role="img" aria-label="Photo d'une équipe d'affaires souriante qui applaudit">
    <p class="hero-cta">Simplifiez votre développement des affaires</p>
    <div class="hero-dots"><span></span><span class="is-current"></span><span></span><span></span><span></span></div>
  </div>
  <a class="hero-arrow prev" href="#" aria-label="Précédent"><svg width="40" height="40" viewBox="0 0 40 40"><path d="M24 11 15 20 24 29" fill="none" stroke="#fff" stroke-width="4"/></svg></a>
  <a class="hero-arrow next" href="#" aria-label="Suivant"><svg width="40" height="40" viewBox="0 0 40 40"><path d="M16 11 25 20 16 29" fill="none" stroke="#fff" stroke-width="4"/></svg></a>
</section>

<span class="pointer" style="left:359px"></span>
<span class="pointer" style="left:574px"></span>
<span class="pointer" style="left:781px"></span>

<main class="features">
  <article class="feature">
    <h2>Pourquoi nous ?</h2>
    <p>Lorem ipsum dolor sit amet, consectetur adipiscing elit. Donec eu magna venenatis, vestibulum purus vel, vehicula arcu. Curabitur accumsan tellus eget luctus imperdiet. Suspendisse elit ipsum, cursus a pulvinar non, elementum ut magna. Aenean eget leo odio. Maecenas facilisis felis dapibus sodales pellentesque. Donec porta velit quis eros placerat, vel congue dui tristique. Curabitur euismod sollicitudin vestibulum...</p>
    <a href="#" class="btn">EN SAVOIR PLUS</a>
  </article>
  <article class="feature">
    <h2>Marketing</h2>
    <p>Lorem ipsum dolor sit amet, consectetur adipiscing elit. Donec eu magna venenatis, vestibulum purus vel, vehicula arcu. Curabitur accumsan tellus eget luctus imperdiet. Suspendisse elit ipsum, cursus a pulvinar non, elementum ut magna. Aenean eget leo odio. Maecenas facilisis felis dapibus sodales pellentesque. Donec porta velit quis eros placerat, vel congue dui tristique. Curabitur euismod sollicitudin vestibulum...</p>
    <a href="#" class="btn">EN SAVOIR PLUS</a>
  </article>
  <article class="feature">
    <h2>Clients</h2>
    <p>Lorem ipsum dolor sit amet, consectetur adipiscing elit. Donec eu magna venenatis, vestibulum purus vel, vehicula arcu. Curabitur accumsan tellus eget luctus imperdiet. Suspendisse elit ipsum, cursus a pulvinar non, elementum ut magna. Aenean eget leo odio. Maecenas facilisis felis dapibus sodales pellentesque. Donec porta velit quis eros placerat, vel congue dui tristique. Curabitur euismod sollicitudin vestibulum...</p>
    <a href="#" class="btn">EN SAVOIR PLUS</a>
  </article>
</main>

<div class="band"></div>

<footer class="site-footer">
  <div class="foot-col" style="left:294px">
    <h3>À propos :</h3>
    <p>Lorem ipsum dolor sit amet, consectetur adipiscing elit. Donec eu magna venenatis, vestibulum purus vel, vehicula arcu. Curabitur accumsan tellus eget luctus.</p>
  </div>
  <div class="foot-col" style="left:506px">
    <h3>Adresse :</h3>
    <p>Lorem ipsum dolor sit amet, consectetur adipiscing elit. Donec eu magna venenatis, vestibulum purus vel, vehicula arcu. Curabitur accumsan tellus eget luctus.</p>
  </div>
  <div class="foot-col" style="left:713px">
    <h3>Nous joindre :</h3>
    <div class="socials"><span></span><span></span><span></span><span></span></div>
  </div>
</footer>

<div class="copyright">Copyright 2013 <strong>Lumivan Conseil</strong></div>
</body>
</html>
```